Commercial janitorial company looking for a fresh and modern website design

We need a new website design for our Edmonton, Alberta-based commercial cleaning company called Brevick Custodial Limited. We have been providing services throughout Alberta for over 50 years, and have a strong customer-oriented service reputation. We are working to re-brand our image and the next crucial piece of that is an informative, simple, and modern website. We provide full service office and industrial cleaning, periodic services, and basic building maintenance, with a focus on being a 'silent partner' for our clients, allowing them to focus on their core business services. We are committed to the highest safety standards and industry best practices for productivity, employing environmentally friendly products practices in all our locations.

We would like a visually pleasing, easy-to-navigate website structure that provides clear communication through imagery and minimal text.

Target Market(s)

Commercial businesses

Industry/Entity Type

It Company

Font styles to use
Other font styles liked:
• Segoe (similar to our logo's font)

Requirements
Must have
• We would like the landing page to be extremely straightforward, with minimal scrolling required, and minimal text presence. We will likely have up to 5 sub-menus / pages, leading off from the main landing page. These pages will have further text on them, supplying further information. We would prefer their location on the top of the screen to be locked or in some way present during any page scrolling.
• Our logos are also available in eps, pdf, ai formats.
Nice to have
• Some websites that we like the presentation of include:
• tanglorn.hr
• quintbrook.com
• vox.com
• morvill.com
• tryplanko.com
• zunor.com

```html
<!DOCTYPE html>
<html lang="en">
<head>
<meta charset="utf-8">
<title>Brevick Custodial Limited</title>
<link href="https://fonts.googleapis.com/css2?family=Open+Sans:ital,wght@0,400;0,600;0,700;1,400&display=swap" rel="stylesheet">
<style>
:root{
  --blue:#1a8fd6;
  --blue-dark:#1479b8;
  --green:#6ab43e;
  --ink:#2b2b2b;
  --muted:#777;
  --light:#f6f6f6;
  --footer:#3a3d42;
  --white:#fff;
}
*{box-sizing:border-box;margin:0;padding:0}
html,body{width:1200px;height:2951px;overflow:hidden}
body{font-family:"Open Sans",sans-serif;color:var(--ink);background:var(--white);position:relative}
section,header,footer{position:absolute;left:0;width:1200px}
.abs{position:absolute}

/* header */
.site-header{top:0;height:104px;background:var(--white);box-shadow:0 2px 4px rgba(0,0,0,.08);z-index:2}
.brand{left:100px;top:30px;display:flex;align-items:center;gap:14px}
.brand-dot{width:40px;height:40px;border-radius:50%;background:var(--blue)}
.brand-name{font-size:22px;font-weight:600;color:#444;letter-spacing:.5px;line-height:1}
.brand-name small{display:block;font-size:11px;letter-spacing:3px;margin-top:4px;font-weight:600}
.main-nav{right:98px;top:44px;display:flex;gap:38px;font-size:14px;font-weight:600}
.main-nav a{color:#222;text-decoration:none}
.main-nav a.active{color:var(--blue)}

/* hero */
.hero{top:104px;height:551px;background:linear-gradient(180deg,#5d7fa6 0%,#9fb4c8 45%,#c9ced2 75%,#6e7a6a 100%)}
.hero-title{top:200px;width:100%;text-align:center;color:var(--white);font-size:40px;font-weight:700;letter-spacing:.5px}
.hero-sub{top:262px;left:170px;width:860px;text-align:center;color:var(--white);font-size:20px;line-height:32px}
.hero-arrow{top:262px;width:44px;height:44px;border-radius:50%;background:rgba(255,255,255,.35)}
.hero-arrow.prev{left:22px}.hero-arrow.next{right:22px}

/* section titles */
.section-title{width:100%;text-align:center;font-size:30px;font-weight:700;text-transform:uppercase}
.section-title span{color:var(--blue)}
.lead{text-align:center;font-size:15px;line-height:27px;color:var(--muted)}

/* what we do */
.services{top:655px;height:525px;background:var(--white)}
.services .section-title{top:30px}
.services .lead{top:84px;left:190px;width:820px}
.service-card{top:244px;width:309px;height:224px;border:1px solid #e3e3e3;text-align:center}
.service-icon{position:absolute;left:89px;top:-100px;width:130px;height:130px;border-radius:50%;background:var(--blue);border:6px solid #e8f3fb;display:flex;align-items:center;justify-content:center}
.service-card h3{margin-top:76px;font-size:20px;font-weight:400;letter-spacing:.5px}
.service-card p{margin:14px auto 0;width:200px;font-size:13px;line-height:24px;color:var(--muted)}
.read-more{display:inline-block;margin-top:14px;font-size:12px;font-weight:600;color:var(--blue);text-decoration:none}

/* where we operate */
.operate{top:1180px;height:437px;background:linear-gradient(180deg,#8a8f94 0%,#b7b6ae 40%,#6f7d62 100%)}
.operate .section-title{top:32px;color:var(--white)}
.slider-arrows{right:100px;top:42px;display:flex;gap:4px}
.slider-arrows i{width:20px;height:20px;background:var(--blue);display:block}
.facility{top:102px;width:242px;height:276px;background:var(--white)}
.facility-photo{height:168px}
.facility h4{margin:16px 14px 0;font-size:17px;font-weight:600}
.facility p{margin:6px 14px 0;font-size:12px;line-height:19px;color:var(--muted)}

/* who we are */
.about{top:1617px;height:468px;background:var(--green);color:var(--white)}
.about .section-title{top:22px;color:var(--white)}
.about h3{left:100px;top:108px;font-size:22px;font-weight:400;letter-spacing:.5px}
.about .intro{left:100px;top:150px;width:480px;font-size:13px;line-height:28px}
.motto-list{left:100px;top:228px;width:500px;list-style:none;font-size:13px}
.motto-list li{display:flex;align-items:center;gap:12px;height:35px}
.btn{left:100px;top:368px;width:152px;height:45px;background:var(--blue);color:var(--white);font-size:15px;font-weight:600;display:flex;align-items:center;justify-content:center;text-decoration:none}
.about-photo{left:614px;top:106px;width:489px;height:309px;border:4px solid rgba(255,255,255,.35);background:linear-gradient(135deg,#e5e9ec 0%,#c4ccd2 55%,#9aa3a8 100%)}

/* work with us */
.team{top:2085px;height:545px;background:var(--light)}
.team .section-title{top:40px}
.team .lead{top:108px;left:190px;width:820px}
.member{top:188px;width:300px;text-align:center}
.avatar{width:154px;height:154px;margin:0 auto;border-radius:50%;border:5px solid var(--white);box-shadow:0 0 0 1px #ddd,0 3px 8px rgba(0,0,0,.15);background:linear-gradient(160deg,#cfd4d8,#8d969c)}
.member h4{margin-top:16px;font-size:20px;font-weight:600}
.member .role{font-size:14px;font-weight:600;color:var(--blue)}
.member p{margin:14px auto 0;width:270px;font-size:12px;font-style:italic;line-height:26px;color:var(--muted)}

/* footer */
.site-footer{top:2630px;height:252px;background:var(--footer);color:#d8d8d8}
.footer-head{font-size:13px;font-weight:700;color:var(--blue);text-transform:uppercase;top:41px}
.footer-brand{left:100px;top:86px;display:flex;align-items:center;gap:12px}
.footer-brand .brand-name{color:var(--white)}
.footer-about{left:100px;top:164px;width:330px;font-size:12px;line-height:26px}
.footer-links{left:458px;top:72px;list-style:none;font-size:12px;line-height:27px}
.social{left:628px;top:78px;display:flex;gap:8px}
.social i{width:32px;height:32px;border-radius:50%;border:2px solid var(--white);display:block}
.contact-list{left:917px;top:72px;list-style:none;font-size:12px;line-height:27px}
.contact-list li{display:flex;gap:12px;align-items:flex-start}
.contact-list svg{margin-top:8px;flex:none}
.bottom-bar{position:absolute;left:0;top:2882px;width:1200px;height:69px;background:var(--blue);color:var(--white);font-size:13px;display:flex;align-items:center;justify-content:center}
</style>
</head>
<body>

<header class="site-header">
  <div class="brand abs"><span class="brand-dot"></span><span class="brand-name">BREVICK<small>CUSTODIAL LIMITED</small></span></div>
  <nav class="main-nav abs">
    <a class="active" href="#">HOME</a><a href="#">WHAT WE DO</a><a href="#">WHERE WE OPERATE</a><a href="#">WHO WE ARE</a><a href="#">WORK WITH US</a><a href="#">CONTACT US</a>
  </nav>
</header>

<section class="hero" role="img" aria-label="Modern glass office building under a blue sky">
  <span class="hero-arrow prev abs"></span><span class="hero-arrow next abs"></span>
  <h1 class="hero-title abs">BREVICK CUSTODIAL LIMITED</h1>
  <p class="hero-sub abs">Since 1963 Brevick Custodial Limited has been providing commercial cleaning services to clients across Alberta.</p>
</section>

<section class="services">
  <h2 class="section-title abs">What we <span>do</span></h2>
  <p class="lead abs">As a full-spectrum janitorial services company, we employ a team-focused, ‘all hands on deck’ approach, wherein every team member is empowered to address client concerns.</p>

  <article class="service-card abs" style="left:98px">
    <div class="service-icon"><svg width="64" height="50" viewBox="0 0 64 50" fill="#fff"><rect x="4" y="24" width="30" height="18" rx="4"/><circle cx="12" cy="44" r="5"/><circle cx="28" cy="44" r="5"/><path d="M34 30 C48 30 46 6 58 6" stroke="#fff" stroke-width="4" fill="none"/><rect x="52" y="2" width="10" height="8" rx="2"/></svg></div>
    <h3>CLEANING CARPETS</h3><p>This allows us to be very flexible and responsive to client needs.</p><a class="read-more" href="#">READ MORE ➜</a>
  </article>
  <article class="service-card abs" style="left:446px">
    <div class="service-icon"><svg width="50" height="64" viewBox="0 0 50 64" fill="#fff"><circle cx="22" cy="9" r="7"/><path d="M12 20h20l4 22h-6v20h-6V44h-2v18h-6V42H8z"/><rect x="36" y="52" width="12" height="10" rx="2"/></svg></div>
    <h3>RESURFACING FLOORS</h3><p>This allows us to be very flexible and responsive to client needs.</p><a class="read-more" href="#">READ MORE ➜</a>
  </article>
  <article class="service-card abs" style="left:793px">
    <div class="service-icon"><svg width="64" height="44" viewBox="0 0 64 44" fill="#fff"><rect x="2" y="4" width="6" height="38"/><rect x="56" y="16" width="6" height="26"/><rect x="8" y="22" width="48" height="12"/><rect x="12" y="12" width="14" height="10" rx="3"/></svg></div>
    <h3>CLEANING FURNITURE</h3><p>This allows us to be very flexible and responsive to client needs.</p><a class="read-more" href="#">READ MORE ➜</a>
  </article>
</section>

<section class="operate" role="img" aria-label="Blurred office lobby background">
  <h2 class="section-title abs">Where we <span>operate</span></h2>
  <div class="slider-arrows abs"><i></i><i></i></div>
  <article class="facility abs" style="left:100px"><div class="facility-photo" role="img" aria-label="Mopping a white tiled floor" style="background:linear-gradient(160deg,#e8eaec,#b9c0c4)"></div><h4>OFFICE FACILITIES</h4><p>Brevick provides services to businesses in all varieties of industries</p></article>
  <article class="facility abs" style="left:354px"><div class="facility-photo" role="img" aria-label="Worker cleaning solar panels" style="background:linear-gradient(160deg,#7a4b4f,#2c4f86)"></div><h4>GOVERNMENT FACILITIES</h4><p>Brevick provides services to businesses in all varieties of industries</p></article>
  <article class="facility abs" style="left:606px"><div class="facility-photo" role="img" aria-label="Cleaner washing a bright glass interior" style="background:linear-gradient(160deg,#f2f3f1,#c8c3b5)"></div><h4>RETAIL FACILITIES</h4><p>Brevick provides services to businesses in all varieties of industries</p></article>
  <article class="facility abs" style="left:860px"><div class="facility-photo" role="img" aria-label="Rope workers cleaning a glass facade" style="background:linear-gradient(160deg,#5a8fc4,#1f5a93)"></div><h4>INDUSTRIAL FACILITIES</h4><p>Brevick provides services to businesses in all varieties of industries</p></article>
</section>

<section class="about">
  <h2 class="section-title abs">Who we <span>are</span></h2>
  <h3 class="abs">STANDING MOTTO</h3>
  <p class="intro abs">We want to be your silent partner’. To this end, our overriding goal is to provide service in a matter that allows our clients to focus solely on their core business activities.</p>
  <ul class="motto-list abs">
    <li><svg width="13" height="13" viewBox="0 0 13 13"><circle cx="6.5" cy="6.5" r="6.5" fill="#fff"/><path d="M3.5 6.8l2 2 4-4.2" stroke="#6ab43e" stroke-width="1.8" fill="none"/></svg>Treat everyone as family.</li>
    <li><svg width="13" height="13" viewBox="0 0 13 13"><circle cx="6.5" cy="6.5" r="6.5" fill="#fff"/><path d="M3.5 6.8l2 2 4-4.2" stroke="#6ab43e" stroke-width="1.8" fill="none"/></svg>Possess the attitude, tools, and knowledge to serve in a professional manner.</li>
    <li><svg width="13" height="13" viewBox="0 0 13 13"><circle cx="6.5" cy="6.5" r="6.5" fill="#fff"/><path d="M3.5 6.8l2 2 4-4.2" stroke="#6ab43e" stroke-width="1.8" fill="none"/></svg>Celebrate behaviour that avoids injury.</li>
  </ul>
  <a class="btn abs" href="#">READ MORE</a>
  <div class="about-photo abs" role="img" aria-label="Cleaner mopping a bright corridor floor"></div>
</section>

<section class="team">
  <h2 class="section-title abs">Work with <span>us</span></h2>
  <p class="lead abs">Brevick is fully devoted to local economic growth and employing a management team that is highly approachable and family-oriented, truly embodying our values.</p>
  <article class="member abs" style="left:80px"><div class="avatar" role="img" aria-label="Portrait of team lead Marlo Fenwick"></div><h4>Marlo Fenwick</h4><div class="role">(Team Lead)</div><p>This enables Brevick to maintain an extremely low staff turnover rate, something we take great pride in.</p></article>
  <article class="member abs" style="left:450px"><div class="avatar" role="img" aria-label="Portrait of team lead Tavish Ordell"></div><h4>Tavish Ordell</h4><div class="role">(Team Lead)</div><p>This enables Brevick to maintain an extremely low staff turnover rate, something we take great pride in.</p></article>
  <article class="member abs" style="left:822px"><div class="avatar" role="img" aria-label="Portrait of team lead Corin Palst"></div><h4>Corin Palst</h4><div class="role">(Team Lead)</div><p>This enables Brevick to maintain an extremely low staff turnover rate, something we take great pride in.</p></article>
</section>

<footer class="site-footer">
  <div class="footer-head abs" style="left:100px">About us</div>
  <div class="footer-brand abs"><span class="brand-dot"></span><span class="brand-name">BREVICK<small>CUSTODIAL LIMITED</small></span></div>
  <p class="footer-about abs">To provide the highest quality cleaning services, based on clearly laid out expectations.</p>

  <div class="footer-head abs" style="left:458px">Links</div>
  <ul class="footer-links abs"><li>Home</li><li>What We Do</li><li>Where We Operate</li><li>Who We Are</li><li>Work With Us</li></ul>

  <div class="footer-head abs" style="left:628px">Follow us</div>
  <div class="social abs"><i style="background:#3b5998"></i><i style="background:#2fa9e0"></i><i style="background:#c4302b"></i><i style="background:#d9453b"></i><i style="background:#c8882c"></i></div>

  <div class="footer-head abs" style="left:917px">Contact us</div>
  <ul class="contact-list abs">
    <li><svg width="10" height="12" viewBox="0 0 10 12"><path d="M5 0a4 4 0 0 1 4 4c0 3-4 8-4 8S1 7 1 4a4 4 0 0 1 4-4z" fill="#fff"/></svg><span>Office: Brevick Limited,<br>PO BOX No City Name, Country</span></li>
    <li><svg width="10" height="12" viewBox="0 0 10 12"><rect x="2" y="0" width="6" height="12" rx="1" fill="#fff"/></svg><span>Mobile: (001) 555-01942</span></li>
    <li><svg width="10" height="12" viewBox="0 0 10 12"><rect x="0" y="3" width="10" height="8" fill="#fff"/><rect x="2" y="0" width="6" height="3" fill="#fff"/></svg><span>Fax: (001) 555-01942</span></li>
    <li><svg width="10" height="12" viewBox="0 0 10 12"><rect x="0" y="3" width="10" height="7" fill="#fff"/></svg><span>Mail: info@brevickmail.com</span></li>
  </ul>
</footer>
<div class="bottom-bar">BREVICK. © 2016 | Privacy Policy</div>

</body>
</html>
```